Brochure for a paper wholesaler who wants to educate his print industry clients

We will be making a stapled informative brochure, that contains basic information about our paper products - the types of paper there is, their characteristics and other useful information.
As we are part of a paper wholesaler group in Europe - VORENT, we received a brochure in German that has this kind of information. The text in it is not as important. What is important is the layout of the document and how the text will appear in it (added in the uploaded files - 210915_Wiessenswertes_TBLK_F51.pdf).
We are allowed to tinker with this file and adjust it to our needs. So there are also .idml and .indd files available (also in the uploaded files).
We would like to keep the custom page size of 210 x290mm (8.3x11.4 in), or you can go up to 210x297mm (8.3x11.7 in).
What we want is a modern looking design that contains our companies red bordo and white/ grey colours to replace the existing green colours in this borchure. The pictures and appearance of the file can be changed according to your views and what you think would look good. We don't necessarily want to keep the same design, we just want the layout of the document be the same, as we will be placing our translated text into it. The VORENT logo should be replaced with our own logo (KUMET Logo.png).
As for how it could look, it could go together with our paper presentation, for which the design can be seen in the "KUMET Base - v2.pptx".
Holiday season, so have a lot of tasks to take care of and not as much time to check ArtHarbor as often.

```html
<!DOCTYPE html>
<html lang="en">
<head>
<meta charset="utf-8">
<title>KUMET brochure – cover and opening spread</title>
<link rel="stylesheet" href="https://fonts.googleapis.com/css2?family=Archivo+Black&family=Bebas+Neue&family=Roboto:wght@300;400;500&display=swap">
<style>
  :root {
    --bordo: #7a1e24;
    --bordo-dark: #5e1419;
    --bordo-light: #93303a;
    --paper: #ffffff;
    --ink: #141414;
    --stage: #e4e4e6;
    --muted: #3a3a3a;
  }
  * { box-sizing: border-box; margin: 0; padding: 0; }
  html, body { width: 857px; height: 1200px; overflow: hidden; }
  body { background: var(--stage); font-family: "Roboto", Arial, sans-serif; color: var(--ink); position: relative; }

  .page { position: absolute; background: var(--paper); overflow: hidden; box-shadow: 0 6px 22px rgba(0,0,0,.12); }

  /* Cover */
  .cover { left: 258px; top: 60px; width: 340px; height: 470px; }
  .cover-art { position: absolute; inset: 0; }
  .brand { position: absolute; left: 36px; top: 96px; display: flex; align-items: center; gap: 12px; }
  .brand-mark { width: 26px; height: 26px; border: 2px solid var(--bordo); }
  .brand-name { font-family: "Roboto", Arial, sans-serif; font-weight: 400; font-size: 15px; letter-spacing: 9px; color: var(--bordo); }
  .cover-headline { position: absolute; left: 120px; top: 282px; font-family: "Bebas Neue", "Arial Narrow", sans-serif; font-weight: 400; color: var(--paper); font-size: 34px; line-height: .95; letter-spacing: .5px; }
  .cover-headline span { display: block; white-space: nowrap; }
  .cover-tagline { position: absolute; left: 120px; top: 392px; color: var(--paper); font-weight: 300; font-size: 14px; letter-spacing: .4px; white-space: nowrap; }

  /* Spread */
  .spread { position: absolute; left: 88px; top: 590px; width: 680px; height: 470px; display: flex; box-shadow: 0 6px 22px rgba(0,0,0,.12); }
  .spread .page { position: relative; width: 340px; height: 470px; box-shadow: none; }
  .spread .page.left { border-right: 1px solid #e2e2e2; }
  .corner { position: absolute; inset: 0; }

  .section-title { font-family: "Archivo Black", Arial, sans-serif; font-size: 17px; letter-spacing: .3px; color: var(--ink); position: absolute; white-space: nowrap; }
  .guide-title { left: 30px; top: 34px; }
  .about-title { left: 0; right: 0; top: 40px; text-align: center; }

  .guide-item { position: absolute; display: flex; flex-direction: column; align-items: center; width: 110px; }
  .hex { width: 38px; height: 42px; clip-path: polygon(50% 0, 100% 25%, 100% 75%, 50% 100%, 0 75%, 0 25%);
         background: linear-gradient(160deg, #c9c9c9, #8a8a8a); display: grid; place-items: center; }
  .hex span { width: 33px; height: 37px; clip-path: polygon(50% 0, 100% 25%, 100% 75%, 50% 100%, 0 75%, 0 25%);
              background: var(--bordo); color: var(--paper); font-family: "Archivo Black", Arial, sans-serif; font-size: 11px;
              display: grid; place-items: center; }
  .guide-label { margin-top: 5px; font-family: "Archivo Black", Arial, sans-serif; font-size: 8px; letter-spacing: .3px; text-transform: uppercase; text-align: center; white-space: nowrap; }

  .fact { position: absolute; width: 130px; display: flex; flex-direction: column; align-items: center; text-align: center; }
  .fact-icon { width: 44px; height: 44px; border-radius: 50%; background: var(--bordo); display: grid; place-items: center; }
  .fact-icon svg { width: 24px; height: 24px; fill: none; stroke: var(--paper); stroke-width: 1.4; stroke-linecap: round; stroke-linejoin: round; }
  .fact-value { margin-top: 6px; font-size: 12px; letter-spacing: .4px; text-transform: uppercase; white-space: nowrap; }
  .fact-note { font-size: 7.5px; color: var(--muted); line-height: 1.25; }
</style>
</head>
<body>

<section class="page cover" aria-label="Brochure cover">
  <svg class="cover-art" viewBox="0 0 340 470" aria-hidden="true">
    <defs>
      <linearGradient id="coverRed" x1="0" y1="0" x2="1" y2="1">
        <stop offset="0" stop-color="#7e2026"/>
        <stop offset="1" stop-color="#64161b"/>
      </linearGradient>
      <linearGradient id="foldRed" x1="0" y1="0" x2="1" y2="1">
        <stop offset="0" stop-color="#9a3540"/>
        <stop offset="1" stop-color="#7a2229"/>
      </linearGradient>
    </defs>
    <polygon points="215,0 340,0 340,470 60,470 92,330 150,205" fill="url(#coverRed)"/>
    <polygon points="215,0 340,0 340,190 255,205 185,160 175,100" fill="url(#foldRed)"/>
    <polygon points="72,278 112,298 112,344 72,366 32,344 32,298" fill="#6f1a20" stroke="#5a1217" stroke-width="1"/>
  </svg>
  <div class="brand">
    <div class="brand-mark"></div>
    <div class="brand-name">KUMET</div>
  </div>
  <h1 class="cover-headline"><span>We help</span><span>Latvian printing</span><span>industry grow</span></h1>
  <p class="cover-tagline">Your growth is our priority!</p>
</section>

<div class="spread" aria-label="Opening spread">
  <section class="page left">
    <svg class="corner" viewBox="0 0 340 470" aria-hidden="true">
      <polygon points="340,320 340,470 255,470" fill="var(--bordo)"/>
    </svg>
    <h2 class="section-title guide-title">PRESENTATION GUIDE</h2>

    <div class="guide-item" style="left:22px; top:100px"><div class="hex"><span>03</span></div><div class="guide-label">About KUMET</div></div>
    <div class="guide-item" style="left:22px; top:175px"><div class="hex"><span>04</span></div><div class="guide-label">KUMET Logistics</div></div>
    <div class="guide-item" style="left:22px; top:250px"><div class="hex"><span>05</span></div><div class="guide-label">KUMET and VORENT</div></div>
    <div class="guide-item" style="left:22px; top:325px"><div class="hex"><span>06</span></div><div class="guide-label">Performance</div></div>

    <div class="guide-item" style="left:168px; top:145px"><div class="hex"><span>08</span></div><div class="guide-label">What we offer</div></div>
    <div class="guide-item" style="left:168px; top:225px"><div class="hex"><span>13</span></div><div class="guide-label">Our suppliers</div></div>
    <div class="guide-item" style="left:168px; top:305px"><div class="hex"><span>14</span></div><div class="guide-label">Our products</div></div>
  </section>

  <section class="page right">
    <svg class="corner" viewBox="0 0 340 470" aria-hidden="true">
      <polygon points="340,40 340,220 285,180" fill="var(--bordo)"/>
    </svg>
    <h2 class="section-title about-title">ABOUT KUMET</h2>

    <div class="fact" style="left:30px; top:100px">
      <div class="fact-icon"><svg viewBox="0 0 24 24"><circle cx="12" cy="9" r="5"/><path d="M9 13l-2 8 5-3 5 3-2-8"/></svg></div>
      <div class="fact-value">1993</div><div class="fact-note">ANNO</div>
    </div>
    <div class="fact" style="left:180px; top:130px">
      <div class="fact-icon"><svg viewBox="0 0 24 24"><circle cx="12" cy="8" r="4"/><path d="M4 21c0-4.5 3.6-7 8-7s8 2.5 8 7"/></svg></div>
      <div class="fact-value">1700+</div><div class="fact-note">Active Costumer</div>
    </div>
    <div class="fact" style="left:30px; top:210px">
      <div class="fact-icon"><svg viewBox="0 0 24 24"><rect x="4" y="10" width="8" height="8"/><rect x="12" y="10" width="8" height="8"/><rect x="8" y="3" width="8" height="7"/></svg></div>
      <div class="fact-value">Over 10000</div><div class="fact-note">Assortment Positions</div>
    </div>
    <div class="fact" style="left:180px; top:235px">
      <div class="fact-icon"><svg viewBox="0 0 24 24"><path d="M6 3h9l4 4v14H6z"/><path d="M15 3v4h4M9 12h7M9 16h7"/></svg></div>
      <div class="fact-value">One stop shop</div><div class="fact-note">Everything for Printing<br>in One Place</div>
    </div>
    <div class="fact" style="left:105px; top:320px">
      <div class="fact-icon"><svg viewBox="0 0 24 24"><circle cx="12" cy="8" r="3"/><circle cx="5.5" cy="10" r="2.3"/><circle cx="18.5" cy="10" r="2.3"/><path d="M7 20c0-3 2.2-5 5-5s5 2 5 5M2 19c0-2 1.4-3.6 3.5-3.6M22 19c0-2-1.4-3.6-3.5-3.6"/></svg></div>
      <div class="fact-value">34</div><div class="fact-note">(2023) Employees</div>
    </div>
  </section>
</div>

</body>
</html>
```